Luxury Ayurvedic Hair Oil logo and package design

We need a logo and package design for our Ayurvedic and natural hair growth oil. Our company, Velmora, is the premier luxury Ayurvedic beauty brand, bringing ancient East-Indian natural and botanic health and beauty products to the US market. Our first major product - Velmora Hair Growth Oil - is a coconut oil based product that was developed by tribes in the Southern State of Kerala that includes ancient herbs like Gooseberry, Indigo, Indian Aloe, Balloon Vine and Brahmi.

The design should be catered to the high-end luxury market (minimal design, minimal text, fonts that invoke a sense of luxury). The primary colors should be deep blue for the packaging and gold for the characters (it's in the name - Velmora). We are looking to sell our products in Brenvale and Tolland Pryce and require packaging that is in line with products sold at these high-end retailers.

The final logo design and packaging should communicate luxury and the ancient wisdom of far-eastern traditions.

Target Market(s)

Velmora's main target is women who value fashionable/quality skincare, beauty, and fragrance products and are open to a medium to high price range. These women love uniqueness in brand and products that cannot be found elsewhere. They are looking for the next new "it" item that will take their haircare and beauty regiment to the next level.

Industry/Entity Type

Hair And Beauty

Font styles to use
Serif

Colors
2f73b3
ffc214

Requirements
Must have
• Must use deep blue (royal blue) background and gold text (to align with brand name). Must use luxurious fonts
Nice to have
• Flowers or other natural symbols, pictures that blend well with the product theme

```html
<!DOCTYPE html>
<html lang="en">
<head>
<meta charset="utf-8">
<title>Velmora Ayurvedic Hair Growth Oil – Labels</title>
<link rel="stylesheet" href="https://fonts.googleapis.com/css2?family=Tenor+Sans&display=swap">
<style>
  :root {
    --canvas-bg: #ffffff;
    --label-navy: #2c2f58;
    --label-navy-edge: #1d1f40;
    --label-black: #1b1b1d;
    --label-black-edge: #0c0c0d;
    --gold: #d6a04a;
    --gold-light: #f0c77a;
    --gold-deep: #a8732a;
    --ink-white: #f4f4f6;
  }
  * { box-sizing: border-box; margin: 0; padding: 0; }
  html, body {
    width: 1200px;
    height: 1200px;
    overflow: hidden;
    background: var(--canvas-bg);
  }
  .canvas {
    position: relative;
    width: 1200px;
    height: 1200px;
    display: flex;
    justify-content: center;
    align-items: center;
    gap: 110px;
  }
  .label {
    position: relative;
    width: 420px;
    height: 640px;
    border-radius: 28px;
    font-family: "Tenor Sans", sans-serif;
    color: var(--ink-white);
    overflow: hidden;
  }
  .label--navy {
    background: linear-gradient(90deg, var(--label-navy-edge) 0%, var(--label-navy) 30%, var(--label-navy) 70%, var(--label-navy-edge) 100%);
  }
  .label--black {
    background: linear-gradient(90deg, var(--label-black-edge) 0%, var(--label-black) 30%, #262628 60%, var(--label-black-edge) 100%);
  }
  .brand-name {
    position: absolute;
    top: 92px;
    left: 0;
    width: 100%;
    text-align: center;
    font-size: 46px;
    letter-spacing: 0.5px;
    color: var(--gold);
  }
  .product-type {
    position: absolute;
    top: 170px;
    left: 0;
    width: 100%;
    text-align: center;
    font-size: 56px;
    letter-spacing: 1px;
    color: var(--ink-white);
  }
  .product-name {
    position: absolute;
    top: 268px;
    left: 52px;
    font-size: 21px;
    line-height: 1.35;
    letter-spacing: 0.3px;
    color: var(--ink-white);
  }
  .botanical-art {
    position: absolute;
    right: 40px;
    top: 262px;
    width: 210px;
    height: 330px;
    border-radius: 110px 110px 20px 110px;
    background: radial-gradient(ellipse at 60% 40%, rgba(240,199,122,0.32) 0%, rgba(214,160,74,0.18) 45%, rgba(168,115,42,0.04) 80%);
  }
  .volume {
    position: absolute;
    left: 52px;
    bottom: 48px;
    font-size: 21px;
    color: var(--ink-white);
  }
</style>
</head>
<body>
  <main class="canvas">
    <section class="label label--navy">
      <p class="brand-name">Velmora</p>
      <h1 class="product-type">AYURVEDIC</h1>
      <p class="product-name">NATURAL HAIR<br>GROWTH OIL</p>
      <div class="botanical-art" role="img" aria-label="Gold line illustration of a leafy botanical sprig with a small flower spike"></div>
      <p class="volume">400mL</p>
    </section>
    <section class="label label--black">
      <p class="brand-name">Velmora</p>
      <h2 class="product-type">AYURVEDIC</h2>
      <p class="product-name">NATURAL HAIR<br>GROWTH OIL</p>
      <div class="botanical-art" role="img" aria-label="Gold line illustration of a leafy botanical sprig with a small flower spike"></div>
      <p class="volume">400mL</p>
    </section>
  </main>
</body>
</html>
```